Online-Marketing Material für Autohaus mit Werkstätten
Zielgruppe
Wir betreiben ein Autohaus mit Werkstätte und suchen hierfür Auszubildende in folgenden Berufen:
Kfz-Mechatroniker, Automobilkaufmann, Fachkraft für Lagerlogistik.
Aufgabenstellung
Die Post sollen Jugendliche ansprechen und sich an dem bisherigen Layout orientieren.

```html
<!DOCTYPE html>
<html lang="de">
<head>
<meta charset="utf-8">
<title>Ausbildung bei auto-kessler</title>
<link href="https://fonts.googleapis.com/css2?family=Roboto:wght@300;400;500;700;900&display=swap" rel="stylesheet">
<style>
  :root {
    --navy: #1d2b6c;
    --ink: #0c0c0c;
    --text: #1a1a1a;
    --accent: #f2ee18;
    --white: #ffffff;
    --photo-light: #f6f7f8;
    --photo-mid: #dfe2e5;
    --photo-dark: #8c9197;
  }
  * { margin: 0; padding: 0; box-sizing: border-box; }
  html, body { width: 1200px; height: 1200px; overflow: hidden; background: var(--white); }
  .post {
    position: relative;
    width: 1200px;
    height: 1200px;
    overflow: hidden;
    font-family: "Roboto", Arial, sans-serif;
    color: var(--text);
  }
  .showroom-photo {
    position: absolute;
    inset: 0;
    background:
      radial-gradient(ellipse 420px 620px at 1010px 650px, rgba(120,125,132,0.55), rgba(120,125,132,0) 70%),
      linear-gradient(90deg, var(--photo-light) 0%, #f1f2f4 30%, var(--photo-mid) 52%, #c4c8cd 72%, var(--photo-dark) 100%);
  }
  .brand {
    position: absolute;
    left: 110px;
    top: 120px;
    display: flex;
    align-items: center;
    gap: 14px;
    font-size: 38px;
    font-weight: 500;
    color: var(--navy);
    letter-spacing: 0.5px;
  }
  .brand-mark {
    width: 26px;
    height: 26px;
    border-radius: 50%;
    background: var(--navy);
  }
  .eyebrow {
    position: absolute;
    left: 114px;
    top: 337px;
    font-size: 23px;
    font-weight: 400;
    letter-spacing: 2.5px;
    color: var(--text);
  }
  .headline {
    position: absolute;
    left: 110px;
    top: 410px;
    font-size: 90px;
    line-height: 87px;
    font-weight: 900;
    letter-spacing: 1px;
    color: var(--ink);
    text-transform: uppercase;
  }
  .headline-slash {
    display: inline-block;
    width: 30px;
    height: 52px;
    margin-left: 22px;
    background: var(--accent);
    transform: skewX(-20deg);
    vertical-align: -2px;
  }
  .positions {
    position: absolute;
    left: 112px;
    top: 693px;
    list-style: none;
    font-size: 38px;
    line-height: 64px;
    font-weight: 400;
    color: var(--text);
  }
  .apply-button {
    position: absolute;
    left: 111px;
    top: 913px;
    width: 540px;
    height: 85px;
    border-radius: 43px;
    background: var(--navy);
    color: var(--white);
    display: flex;
    align-items: center;
    justify-content: center;
    padding-right: 80px;
    font-size: 26px;
    font-weight: 700;
    letter-spacing: 1px;
    text-decoration: none;
  }
  .contact {
    position: absolute;
    top: 1090px;
    display: flex;
    align-items: center;
    gap: 20px;
    font-size: 23px;
    color: var(--text);
  }
  .contact-web { left: 111px; }
  .contact-mail { left: 589px; }
  .contact-icon {
    width: 54px;
    height: 54px;
    border-radius: 50%;
    background: var(--navy);
    display: flex;
    align-items: center;
    justify-content: center;
    flex: none;
  }
  .more-arrows {
    position: absolute;
    left: 1022px;
    top: 1100px;
  }
</style>
</head>
<body>
<main class="post">
  <div class="showroom-photo" role="img" aria-label="Autohaus-Showroom: lächelnder junger Mann im grauen Nadelstreifenanzug hockt neben einem weißen Auto"></div>

  <div class="brand"><span class="brand-mark"></span>auto-kessler</div>

  <p class="eyebrow">AUSBILDUNG</p>

  <h1 class="headline">Lust auf<br>eine Ausbildung<br>bei uns?<span class="headline-slash"></span></h1>

  <ul class="positions">
    <li>KFZ-Mechatroniker (m/w/d) /</li>
    <li>Automobilkaufmann (m/w/d) /</li>
    <li>Fachkraft für Lagerlogistik (m/w/d)</li>
  </ul>

  <a class="apply-button" href="#">JETZT BEWERBEN !</a>

  <div class="contact contact-web">
    <span class="contact-icon">
      <svg width="32" height="32" viewBox="0 0 32 32" fill="none" stroke="#ffffff" stroke-width="2">
        <circle cx="16" cy="16" r="13"/>
        <ellipse cx="16" cy="16" rx="6" ry="13"/>
        <line x1="3" y1="16" x2="29" y2="16"/>
        <line x1="5" y1="9" x2="27" y2="9"/>
        <line x1="5" y1="23" x2="27" y2="23"/>
        <line x1="16" y1="3" x2="16" y2="29"/>
      </svg>
    </span>
    <span>www.kfzjobs.autokessler.de</span>
  </div>

  <div class="contact contact-mail">
    <span class="contact-icon">
      <svg width="34" height="34" viewBox="0 0 34 34" fill="none" stroke="#ffffff" stroke-width="2">
        <circle cx="17" cy="17" r="15"/>
        <rect x="9" y="11.5" width="16" height="11" rx="1"/>
        <polyline points="9,12 17,18 25,12"/>
      </svg>
    </span>
    <span>jkessler@autokessler.de</span>
  </div>

  <svg class="more-arrows" width="74" height="40" viewBox="0 0 74 40" fill="none" stroke="#f2ee18" stroke-width="3">
    <polyline points="4,4 18,20 4,36"/>
    <polyline points="28,4 42,20 28,36"/>
    <polyline points="52,4 66,20 52,36"/>
  </svg>
</main>
</body>
</html>
```